Audit/Compliance company needs Business Card Template

We are after a Business Card Template that we can modify internally to update details as people change positions.
We are an Australian based company specalising in Auditing and Quality/OHS systems development. - See www.kelvaranorth.com.au for more information
We would like the desings to be based around our logo and colours assocaited with it (attached for your information) however we are very open as to how the cards are designed.
We are looking for something quite edgy and mordern but it must have a professional/compliance feel to it (if possible).
The main details we would like to include within the card template are:
Name
Position Title
Postal Address
Phone Number
Mobile Number
Email Address
Website
The cards will be printed through tally press on Glossy paper so it should reflect the requirements below
Full Bleed Size (starting document size)
90 x 52 mm
1062 x 615 pixels
Document Trim Size (final size after being cut)
87 x 49 mm
1028 x 579 pixels
Resolution
300 DPI

```html
<!DOCTYPE html>
<html lang="en">
<head>
<meta charset="utf-8">
<title>Kelvara North Audit &amp; Compliance — Business Card</title>
<link rel="stylesheet" href="https://fonts.googleapis.com/css2?family=Libre+Baskerville&family=Open+Sans:wght@300;400&display=swap">
<style>
  :root {
    --backdrop: #e9e7e4;
    --card: #fbfbfa;
    --ink: #555555;
    --ink-dark: #3d3d3d;
    --blue: #2aa7d4;
    --yellow: #f6b622;
    --rule: #c9c9c9;
    --serif: "Libre Baskerville", Georgia, serif;
    --sans: "Open Sans", Arial, sans-serif;
  }
  * { box-sizing: border-box; margin: 0; padding: 0; }
  html, body { width: 1200px; height: 720px; overflow: hidden; }
  body {
    background: var(--backdrop);
    position: relative;
    font-family: var(--sans);
    color: var(--ink);
  }
  .card {
    position: absolute;
    top: 208px;
    width: 540px;
    height: 304px;
    background: var(--card);
    box-shadow: 0 6px 18px rgba(0,0,0,0.18);
  }
  .card--front { left: 40px; }
  .card--back { left: 620px; }

  /* Front face */
  .front-brand {
    position: absolute;
    left: 118px;
    top: 118px;
    display: flex;
    align-items: center;
    gap: 14px;
  }
  .brand-mark {
    width: 64px;
    height: 64px;
    background: var(--blue);
  }
  .brand-divider {
    width: 1px;
    height: 62px;
    background: var(--rule);
  }
  .brand-name {
    font-family: var(--serif);
    color: var(--ink);
    text-transform: uppercase;
    line-height: 1.2;
  }
  .brand-name__main { font-size: 21px; letter-spacing: 0.5px; display: block; }
  .brand-name__sub { font-size: 11px; letter-spacing: 1.5px; display: block; margin-left: 6px; }

  /* Back face */
  .back-brand {
    position: absolute;
    left: 40px;
    top: 112px;
    display: flex;
    align-items: center;
    gap: 10px;
  }
  .back-brand__dot {
    width: 18px;
    height: 18px;
    border-radius: 50%;
    background: var(--yellow);
  }
  .back-brand__name {
    font-family: var(--serif);
    font-size: 17px;
    color: var(--ink);
    text-transform: uppercase;
    line-height: 1.3;
  }
  .back-divider {
    position: absolute;
    left: 262px;
    top: 62px;
    width: 1px;
    height: 118px;
    background: var(--rule);
  }
  .contact {
    position: absolute;
    left: 278px;
    top: 60px;
  }
  .contact__name {
    font-size: 19px;
    font-weight: 300;
    color: var(--ink-dark);
    line-height: 1;
  }
  .contact__name em { font-style: normal; color: var(--blue); }
  .contact__title {
    font-size: 10px;
    color: var(--ink);
    margin: 2px 0 10px 60px;
  }
  .contact__list { list-style: none; }
  .contact__item {
    display: flex;
    align-items: center;
    gap: 8px;
    font-size: 10.5px;
    line-height: 17px;
  }
  .contact__item svg { width: 10px; height: 10px; fill: var(--blue); flex: none; }
  .address {
    position: absolute;
    right: 22px;
    bottom: 16px;
    display: flex;
    align-items: center;
    gap: 6px;
    font-size: 10.5px;
  }
  .address svg { width: 10px; height: 13px; fill: var(--blue); }
</style>
</head>
<body>

<section class="card card--front" aria-label="Card front">
  <div class="front-brand">
    <div class="brand-mark" aria-hidden="true"></div>
    <div class="brand-divider"></div>
    <h1 class="brand-name">
      <span class="brand-name__main">Kelvara North Audit</span>
      <span class="brand-name__sub">&amp; Compliance</span>
    </h1>
  </div>
</section>

<section class="card card--back" aria-label="Card back">
  <div class="back-brand">
    <div class="back-brand__dot" aria-hidden="true"></div>
    <p class="back-brand__name">Kelvara North</p>
  </div>

  <div class="back-divider"></div>

  <div class="contact">
    <p class="contact__name">John <em>Smith</em></p>
    <p class="contact__title">your title</p>
    <ul class="contact__list">
      <li class="contact__item">
        <svg viewBox="0 0 10 10"><path d="M2 0.5 L3.6 2.6 L2.7 3.8 Q3.8 6 6.2 7.3 L7.4 6.4 L9.5 8 L8.4 9.5 Q4.2 9.2 0.5 1.6 Z"/></svg>
        234-345-234
      </li>
      <li class="contact__item">
        <svg viewBox="0 0 10 10"><rect x="2.5" y="0" width="5" height="10" rx="1"/><rect x="3.3" y="1.2" width="3.4" height="6.2" fill="#fbfbfa"/></svg>
        023-234-452
      </li>
      <li class="contact__item">
        <svg viewBox="0 0 10 10"><circle cx="5" cy="5" r="4.6"/><path d="M0.6 5 H9.4 M5 0.4 V9.6 M1.6 2.6 H8.4 M1.6 7.4 H8.4" stroke="#fbfbfa" stroke-width="0.7" fill="none"/></svg>
        www.kelvaranorth.com.au
      </li>
      <li class="contact__item">
        <svg viewBox="0 0 10 10"><rect x="0" y="1.5" width="10" height="7"/><path d="M0.4 2 L5 5.6 L9.6 2" stroke="#fbfbfa" stroke-width="0.8" fill="none"/></svg>
        e-mail@website.com
      </li>
    </ul>
  </div>

  <p class="address">
    <svg viewBox="0 0 10 13"><path d="M5 0 A5 5 0 0 1 10 5 Q10 8 5 13 Q0 8 0 5 A5 5 0 0 1 5 0 Z"/><circle cx="5" cy="5" r="1.8" fill="#fbfbfa"/></svg>
    your address will be here
  </p>
</section>

</body>
</html>
```